Letterhead & logo design project

We need a letterhead for a new company called Brackenwold Ltd a firm of Chartered Accountants and Chartered Tax Advisers based in Pangbourne, Berkshire
Updates
Please include the following:
Chartered Accountants and Chartered Tax Advisers
Industry/Entity Type
It Company
Requirements
Must have
- Must have director's name at the bottom of the letterhead. Must also contain some wording at the bottom of the page to be provided by the NPRFA at a later date

```html
<!DOCTYPE html>
<html lang="en">
<head>
<meta charset="utf-8">
<title>Brackenwold Ltd – Letterhead</title>
<link rel="stylesheet" href="https://fonts.googleapis.com/css2?family=Tinos:ital,wght@0,700;1,700&family=Arimo:wght@400&display=swap">
<style>
  :root {
    --backdrop: #734800;
    --paper: #ffffff;
    --aqua: #5ff2ea;
    --aqua-soft: #bafff3;
    --aqua-mist-front: rgba(200, 250, 246, 0.75);
    --aqua-mist-back: rgba(235, 255, 251, 0.8);
    --slate: #485356;
    --ink: #111111;
  }
  * { box-sizing: border-box; margin: 0; padding: 0; }
  html, body { width: 1200px; height: 793px; overflow: hidden; }
  body {
    background: var(--backdrop);
    position: relative;
    font-family: "Arimo", Arial, sans-serif;
  }
  .sheet {
    position: absolute;
    top: 34px;
    width: 528px;
    height: 740px;
    overflow: hidden;
  }
  .sheet--front { left: 73px; background: var(--paper); }
  .sheet--back { left: 631px; background: var(--aqua-soft); }

  .brand-mist {
    position: absolute;
    left: 200px;
    top: 350px;
    width: 330px;
    height: 380px;
    border-radius: 50%;
  }
  .sheet--front .brand-mist {
    background: radial-gradient(ellipse at center, var(--aqua-mist-front) 0%, rgba(200, 250, 246, 0.35) 45%, rgba(255, 255, 255, 0) 70%);
  }
  .sheet--back .brand-mist {
    background: radial-gradient(ellipse at center, var(--aqua-mist-back) 0%, rgba(235, 255, 251, 0.35) 45%, rgba(186, 255, 243, 0) 70%);
  }

  .brand {
    position: absolute;
    left: 61px;
    top: 40px;
    display: flex;
    align-items: center;
    gap: 9px;
  }
  .brand__dot {
    width: 28px;
    height: 28px;
    border-radius: 50%;
    background: var(--aqua);
  }
  .brand__name {
    font-family: "Tinos", "Times New Roman", serif;
    font-weight: 700;
    font-size: 26px;
    line-height: 1;
    color: var(--slate);
  }
  .tagline {
    position: absolute;
    left: 61px;
    top: 81px;
    font-family: "Tinos", "Times New Roman", serif;
    font-style: italic;
    font-weight: 700;
    font-size: 10.5px;
    color: var(--aqua);
  }
  .signatory {
    position: absolute;
    left: 62px;
    top: 601px;
    font-family: "Tinos", "Times New Roman", serif;
    font-style: italic;
    font-weight: 700;
    font-size: 10px;
    color: var(--slate);
  }
  .regulatory-note {
    position: absolute;
    left: 62px;
    top: 651px;
    width: 412px;
    font-size: 8.6px;
    line-height: 12px;
    color: var(--ink);
  }
  .footer-band {
    position: absolute;
    left: 0;
    bottom: 0;
    width: 100%;
    height: 27px;
    background: var(--slate);
  }
</style>
</head>
<body>
  <section class="sheet sheet--front" aria-label="Letterhead front">
    <div class="brand-mist" role="img" aria-label="Faint brand decoration area"></div>
    <header class="brand">
      <span class="brand__dot" aria-hidden="true"></span>
      <span class="brand__name">Brackenwold Ltd</span>
    </header>
    <p class="tagline">Chartered Accountants and Chartered Tax Advisers</p>

    <p class="signatory">(Director)</p>
    <p class="regulatory-note">Lorem ipsum dolor sit amet, consectetuer adipiscing elit, sed diam nonummy nibh euismod tincidunt ut laoreet dolore magna aliquam erat volutpat. Ut wisi enim ad minim veniam, quis nostrud exerci tation ullamcorper suscipit lobortis nisl ut aliquip ex ea commodo consequat. Lorem ipsum dolor sit amet, consectetuer adipiscing elit, sed diam nonummy nibh euismod tincidunt ut laoreet.</p>
    <div class="footer-band"></div>
  </section>

  <section class="sheet sheet--back" aria-label="Letterhead reverse">
    <div class="brand-mist" role="img" aria-label="Faint brand decoration area"></div>
  </section>
</body>
</html>
```